Exclusive British Dental Clinic Needs Modern Brochure to Attract New Patients

We are looking to create a smart, sophisticated brochure that gives the public and future potential clients a concise overview of what we offer and why the quality and care on offer is a step above the rest. We are based in the United Kingdom where the Public Wellness Board provide dental care free or at low cost. We are NOT an PWB provider. We are a wholly private dental clinic so all of our patients are paying full-price premium prices directly out of pocket. The work we do is exceptional so all of our patients can be assured that anything we do is done to the highest and best quality possible.
We offer high quality dental treatment using the best and latest techniques, materials and an award winning dental laboratory. All treatments are undertaken using high quality magnification to ensure the best possible result. We have over 30 years’ experience in general dentistry with fully trained staff. In quality comfortable surroundings, we are a caring practice with excellent patient care. We allow more time with our patients and we understand and care for nervous patients.
We also offer facial fillers, wrinkle reducers and teeth whitening in order to help our patients achieve their best look.

We have attached our logo and logo icons to this brief.
We also have attached some information in our Brochure Details document. This just highlights what we would like to see and more information about us.
We are really up to suggestion with design and wording because we want this brochure to be attractive and appealing to the public.
Feel free to edit as you see fit to help us attain our goals :)

Reason: Hello We are very excited about the work we have received thus far...our Practice Manager is away for the next week and we wanted to make sure we are all on board for the discussions and decisions we make moving forward. Thank you for taking the time to help us create our voice! --- Larkmoor Atelier Dental Clinic

```html
<!DOCTYPE html>
<html lang="en">
<head>
<meta charset="utf-8">
<title>Larkmoor Atelier Dental Clinic – Brochure</title>
<link rel="stylesheet" href="https://fonts.googleapis.com/css2?family=Open+Sans:wght@300;400;600;700;800&display=swap">
<style>
  :root {
    --page-bg: #e6e9ec;
    --navy: #1d4f7c;
    --deep-navy: #123e63;
    --bright-blue: #1e8fd6;
    --sky: #a9d3f0;
    --pale-sky: #cfe6f7;
    --mid-blue: #6fb8e8;
    --strip-blue: #3b6f96;
    --ink: #4a5560;
    --white: #ffffff;
    --panel-w: 250px;
    --panel-h: 530px;
  }
  * { box-sizing: border-box; margin: 0; padding: 0; }
  html, body {
    width: 1200px; height: 1152px; overflow: hidden;
    background: var(--page-bg);
    font-family: "Open Sans", Arial, sans-serif;
  }
  .sheet-row { position: absolute; display: flex; box-shadow: 0 6px 18px rgba(0,0,0,.18); }
  .inside-spread { left: 225px; top: 30px; }
  .outside-spread { left: 350px; top: 592px; }
  .panel { width: var(--panel-h); height: var(--panel-h); position: relative; overflow: hidden; }
  .panel { width: var(--panel-w); }

  /* FAQ panel */
  .faq-panel { background: var(--white); padding: 26px 20px 0; }
  .faq-title { color: var(--bright-blue); font-weight: 800; font-size: 30px; line-height: 1; margin-bottom: 10px; }
  .faq-item { margin-bottom: 7px; }
  .faq-question { color: var(--navy); font-weight: 700; font-size: 8.5px; line-height: 1.3; }
  .faq-answer { color: var(--ink); font-size: 7.5px; line-height: 1.35; }
  .faq-photo {
    position: absolute; left: 0; bottom: 0; width: 100%; height: 150px;
    background: linear-gradient(160deg, #f4f6f8 0%, #e3dcd3 55%, #cbbfae 100%);
  }

  /* Cosmetic dentistry double panel */
  .cosmetic-spread { width: calc(var(--panel-w) * 2); height: var(--panel-h); position: relative; background: var(--mid-blue); overflow: hidden; }
  .cosmetic-top { display: flex; height: 190px; }
  .cosmetic-intro { width: var(--panel-w); background: var(--pale-sky); padding: 70px 20px 0; color: var(--white); font-size: 10px; line-height: 1.5; font-weight: 400; }
  .cosmetic-photo { width: var(--panel-w); background: linear-gradient(150deg, #e7f1fa 0%, #bcd9ef 50%, #8fc0e6 100%); }
  .cosmetic-title {
    position: absolute; left: 22px; top: 168px;
    color: var(--bright-blue); font-weight: 800; font-size: 46px; letter-spacing: -1px; line-height: 1;
    text-shadow: 2px 2px 0 var(--white);
  }
  .treatments { position: absolute; left: 22px; right: 22px; top: 238px; color: var(--white); }
  .treatments-heading { font-size: 19px; font-weight: 700; margin-bottom: 16px; }
  .treatment-row { display: flex; justify-content: space-between; font-size: 15px; font-weight: 400; padding: 8px 0; border-bottom: 1px solid rgba(255,255,255,.35); }
  .treatment-price { font-weight: 600; }
  .cosmetic-footer {
    position: absolute; left: 0; right: 0; bottom: 0; height: 46px;
    background: var(--strip-blue); color: var(--white);
    font-size: 9px; display: flex; align-items: center; justify-content: flex-end; padding-right: 20px;
  }

  /* Back panel */
  .back-panel { background: var(--deep-navy); color: var(--white); padding: 70px 24px 0; text-align: center; }
  .brand-mark { display: flex; align-items: center; justify-content: center; gap: 10px; margin-bottom: 40px; }
  .brand-dot { width: 16px; height: 16px; border-radius: 50%; background: var(--sky); flex: none; }
  .brand-name-light { color: var(--white); font-weight: 400; font-size: 14px; letter-spacing: 1px; text-transform: uppercase; line-height: 1.3; text-align: left; }
  .contact { list-style: none; font-size: 11px; line-height: 1.9; color: var(--sky); font-weight: 400; }
  .back-waves { position: absolute; left: 0; bottom: 0; width: 100%; height: 120px; }

  /* Front cover */
  .cover-panel { background: var(--white); }
  .cover-header { height: 150px; display: flex; align-items: center; justify-content: center; gap: 12px; padding: 0 18px; }
  .brand-name-dark { color: var(--navy); font-weight: 400; font-size: 15px; letter-spacing: 1px; text-transform: uppercase; line-height: 1.3; }
  .cover-photo {
    position: absolute; left: 0; top: 150px; width: 100%; height: 380px;
    background: linear-gradient(170deg, #efefef 0%, #e4d2c4 45%, #b98c73 80%, #2d3b55 100%);
  }
  .cover-web { position: absolute; left: 0; right: 0; bottom: 18px; text-align: center; color: var(--white); font-size: 14px; font-weight: 400; }
</style>
</head>
<body>

<section class="sheet-row inside-spread">
  <article class="panel faq-panel">
    <h2 class="faq-title">FAQs</h2>
    <div class="faq-item">
      <p class="faq-question">What is involved in an initial consultation?</p>
      <p class="faq-answer">Your first visit includes a full examination of teeth, gums and soft tissues, with time to discuss your goals and concerns.</p>
    </div>
    <div class="faq-item">
      <p class="faq-question">How often should I see the dentist?</p>
      <p class="faq-answer">We advise a check-up every six months so small problems are found early and treated simply.</p>
    </div>
    <div class="faq-item">
      <p class="faq-question">Why should I choose private dental care?</p>
      <p class="faq-answer">Private care gives longer appointments, the latest materials and a dentist who knows you. We never rush treatment and plan each step with care.</p>
    </div>
    <div class="faq-item">
      <p class="faq-question">What happens during a scale and polish?</p>
      <p class="faq-answer">Our hygienist removes plaque and tartar, then polishes the teeth smooth to help keep gums healthy.</p>
    </div>
    <div class="faq-item">
      <p class="faq-question">Is tooth whitening safe?</p>
      <p class="faq-answer">Yes. When carried out by a dentist, whitening is safe and gentle on enamel.</p>
    </div>
    <div class="faq-item">
      <p class="faq-question">What are facial fillers?</p>
      <p class="faq-answer">Fillers soften lines and restore lost volume for a fresh, natural look.</p>
    </div>
    <div class="faq-photo" role="img" aria-label="Photograph of a smiling fair-haired woman resting her face on her hands"></div>
  </article>

  <article class="cosmetic-spread">
    <div class="cosmetic-top">
      <p class="cosmetic-intro">We offer a full range of treatment options in cosmetic dentistry and facial cosmetic rejuvenation. Looking good often translates into feeling good.</p>
      <div class="cosmetic-photo" role="img" aria-label="Photograph of a smiling woman with her hands beside her face, tinted blue"></div>
    </div>
    <h2 class="cosmetic-title">Cosmetic Dentistry</h2>
    <div class="treatments">
      <h3 class="treatments-heading">Treatments Include</h3>
      <div class="treatment-row"><span>Teeth Whitening</span><span class="treatment-price">£150.00</span></div>
      <div class="treatment-row"><span>Veneers</span><span class="treatment-price">from £225.00</span></div>
      <div class="treatment-row"><span>Tooth Coloured Fillings</span><span class="treatment-price">from £75.00</span></div>
      <div class="treatment-row"><span>Crowns</span><span class="treatment-price">from £295.00</span></div>
    </div>
    <p class="cosmetic-footer">*Prices are a guide only and may vary. We are a mercury free practice*</p>
  </article>
</section>

<section class="sheet-row outside-spread">
  <article class="panel back-panel">
    <div class="brand-mark">
      <span class="brand-dot"></span>
      <span class="brand-name-light">Larkmoor Atelier<br>Dental Clinic</span>
    </div>
    <ul class="contact">
      <li>14 Larkmoor Lane</li>
      <li>Halbury, Wessex</li>
      <li>HB4 7QT</li>
      <li>tel. 01632 960 418</li>
      <li>website www.larkmooratelier.co.uk</li>
      <li>email enquiries@larkmooratelier.co.uk</li>
    </ul>
    <svg class="back-waves" viewBox="0 0 250 120" preserveAspectRatio="none" aria-hidden="true">
      <path d="M0 40 L250 0 L250 120 L0 120 Z" fill="#1e6aa8"/>
      <path d="M0 80 L250 45 L250 120 L0 120 Z" fill="#2d86c9"/>
    </svg>
  </article>

  <article class="panel cover-panel">
    <header class="cover-header">
      <span class="brand-dot"></span>
      <span class="brand-name-dark">Larkmoor Atelier<br>Dental Clinic</span>
    </header>
    <div class="cover-photo" role="img" aria-label="Photograph of a smiling dark-haired young woman"></div>
    <p class="cover-web">www.larkmooratelier.co.uk</p>
  </article>
</section>

</body>
</html>
```